Flyer Design sales and lettings

We need a double sided flyer for our Estate and Letting agency. We have just moved in to 16th century office and expanded our offer to commercial and residential sales (previously we were targeted on lettings only). We are based in small rural town in Midlands, UK.Any photos, graphics will need to be linked to our location (please dont use skyscrapers :)One side of our flyer will have to treat about lettings and our offer - 7% plus vat commission on all new lettings, no extra costs, rent guarantee insurance, we are open 6 days a week and available 24/7.Please insert information about our commercial department on this side as well. "Landlords! Did you know that we also do commercial lettings? Call us on 01592738164 for best offer in the area. Other side informing clients about our sales offer 0.7% plus vat on all new sales instructions, free market appraisal, no up front costs, no sale no fee, we are open 6 days a week and available 24/7Here is our website: www.hollowbrookhomes.uk We are members of KLT, WMA and leasewell (logos attached)Thank you Tomasz Welbarek

Target Market(s)

Landlords and vendors in local area

Industry/Entity Type

Real Estate Agent

Font styles to use
Decorative
Script

Requirements
Must have
• all points stated in descriptip
Nice to have
• our logo or parts of it incorporated in design, elegant retro, stylish effcts.
• Silver/Charcoal coulour with retro gold theme.
Should not have
• modern, city accents.

```html
<!DOCTYPE html>
<html lang="en">
<head>
<meta charset="utf-8">
<title>Hollowbrook Homes – Lettings Flyer</title>
<link rel="stylesheet" href="https://fonts.googleapis.com/css2?family=Oswald:wght@500;600&family=Arimo:wght@400;700&family=Lato:ital,wght@1,400;1,700;1,900&family=Playfair+Display:wght@500&display=swap">
<style>
  :root{
    --charcoal:#3f4247;
    --charcoal-dark:#2c2e32;
    --gold:#d99a1c;
    --gold-light:#f3c94a;
    --gold-deep:#b8741a;
    --silver:#e9e9ea;
    --silver-mid:#c9cacc;
    --white:#ffffff;
    --ink:#1b1b1b;
    --logo-brown:#8a6a3c;
  }
  *{margin:0;padding:0;box-sizing:border-box}
  html,body{width:900px;height:1200px;overflow:hidden;background:#fff}
  .flyer{position:relative;width:900px;height:1200px;overflow:hidden;font-family:"Arimo",Arial,sans-serif;background:linear-gradient(#ffffff,#eeeeee)}
  .backdrop{position:absolute;inset:0}
  .portrait{position:absolute;left:0;top:0;width:330px;height:385px;background:linear-gradient(120deg,#d9dde2 0%,#c7b5a4 45%,#4a5464 100%)}
  .brand{position:absolute;left:520px;top:165px;font-family:"Playfair Display",Georgia,serif;font-size:30px;color:var(--logo-brown);display:flex;align-items:center;gap:10px}
  .brand .mark{width:14px;height:14px;background:var(--logo-brown)}
  .headline{position:absolute;left:10px;top:430px;width:440px;text-align:center;font-family:"Oswald",Impact,sans-serif;line-height:1.1;white-space:nowrap}
  .headline .line1{display:block;color:var(--white);font-size:44px;font-weight:600;letter-spacing:.3px}
  .headline .line2{display:block;color:var(--gold-light);font-size:36px;font-weight:600;letter-spacing:1px}
  .offer-bar{position:absolute;left:0;top:550px;width:456px;height:40px;background:linear-gradient(90deg,var(--gold-deep),var(--gold-light) 50%,var(--gold-deep));color:var(--ink);font-weight:700;font-size:19px;text-align:center;line-height:40px}
  .benefits{position:absolute;left:38px;top:602px;list-style:none;color:var(--white);font-weight:700;font-size:26px;line-height:1.18}
  .benefits li{position:relative;padding-left:26px;margin-bottom:12px}
  .benefits li::before{content:"";position:absolute;left:0;top:9px;width:12px;height:12px;border-radius:50%;background:var(--gold-light)}
  .listing-photo{position:absolute;left:512px;top:394px;width:340px;height:136px;border:3px solid var(--white);border-radius:14px;background:linear-gradient(180deg,#7fb3e6 0%,#b86a52 45%,#e9e6e0 70%,#4e7a35 100%)}
  .listing-copy{position:absolute;left:512px;top:548px;width:370px;font-family:"Lato",Arial,sans-serif;font-style:italic;color:var(--white);font-size:16.5px;line-height:1.3}
  .listing-copy .cta{display:block;font-weight:900;font-size:23px;color:var(--ink);margin:8px 0 2px}
  .open-bar{position:absolute;left:0;top:810px;width:470px;height:52px;background:linear-gradient(var(--white),var(--silver-mid));clip-path:polygon(0 0,100% 0,94% 100%,0 100%);font-weight:700;font-size:26px;color:var(--charcoal-dark);line-height:52px;padding-left:30px;white-space:nowrap}
  .available-bar{position:absolute;left:0;top:928px;width:470px;height:62px;background:linear-gradient(var(--white),var(--silver-mid));font-size:34px;color:var(--ink);line-height:62px;padding-left:125px}
  .starburst{position:absolute;left:468px;top:890px;width:145px;height:145px}
  .starburst span{position:absolute;inset:0;display:flex;align-items:center;justify-content:center;font-family:"Oswald",Impact,sans-serif;font-weight:600;font-size:48px;color:var(--ink)}
  .commercial{position:absolute;left:606px;top:812px;width:288px;text-align:center;color:var(--ink);white-space:nowrap}
  .commercial .ask{font-weight:700;font-size:16.5px;line-height:1.3;padding-bottom:8px;border-bottom:1px solid #777}
  .commercial .call{font-weight:700;font-size:25px;margin-top:6px}
  .commercial .phone{font-weight:700;font-size:40px;letter-spacing:.5px;padding-bottom:6px;border-bottom:1px solid #777}
  .commercial .best{font-weight:700;font-size:17px;margin-top:6px}
  .socials{position:absolute;left:0;top:1108px;width:900px;display:flex;justify-content:center;gap:34px;font-size:14px;font-weight:700;color:var(--charcoal)}
  .socials span{display:flex;align-items:center;gap:6px}
  .socials span::before{content:"";width:10px;height:10px;border-radius:50%;background:var(--charcoal)}
  .partners{position:absolute;left:0;top:1144px;width:900px;display:flex;justify-content:space-around;align-items:center;padding:0 50px;font-weight:700;font-size:22px;color:var(--charcoal)}
  .partners span{display:flex;align-items:center;gap:8px}
  .partners span::before{content:"";width:14px;height:14px;background:var(--charcoal)}
</style>
</head>
<body>
<main class="flyer">
  <svg class="backdrop" width="900" height="1200" viewBox="0 0 900 1200" aria-hidden="true">
    <defs>
      <linearGradient id="goldGrad" x1="0" y1="0" x2="1" y2="1">
        <stop offset="0" stop-color="#b8741a"/><stop offset=".5" stop-color="#f3c94a"/><stop offset="1" stop-color="#c8861c"/>
      </linearGradient>
      <linearGradient id="charcoalGrad" x1="0" y1="0" x2="0" y2="1">
        <stop offset="0" stop-color="#4a4d52"/><stop offset="1" stop-color="#2c2e32"/>
      </linearGradient>
      <linearGradient id="silverGrad" x1="0" y1="0" x2="1" y2="1">
        <stop offset="0" stop-color="#ffffff"/><stop offset="1" stop-color="#c9cacc"/>
      </linearGradient>
    </defs>
    <polygon points="0,372 900,336 900,378 0,398" fill="url(#goldGrad)"/>
    <rect x="0" y="396" width="456" height="400" fill="url(#charcoalGrad)"/>
    <rect x="456" y="376" width="444" height="420" fill="url(#goldGrad)"/>
    <rect x="0" y="796" width="456" height="215" fill="url(#charcoalGrad)"/>
    <polygon points="456,796 900,796 900,1050 456,1010" fill="url(#silverGrad)"/>
    <polygon points="0,1005 456,985 900,1060 900,1092 456,1012 0,1038" fill="url(#goldGrad)"/>
    <rect x="0" y="1182" width="900" height="18" fill="url(#goldGrad)"/>
  </svg>

  <div class="portrait" role="img" aria-label="Photo of a thoughtful businesswoman in a light office"></div>

  <div class="brand"><span class="mark"></span>Hollowbrook Homes</div>

  <h1 class="headline">
    <span class="line1">PREVIOUSLY MARLCOMBE</span>
    <span class="line2">LETTING AGENTS LTD</span>
  </h1>

  <div class="offer-bar">XPANDED OUR OFFER</div>

  <ul class="benefits">
    <li>7% plus vat commission<br>on all new lettings</li>
    <li>No extra costs</li>
    <li>Rent guarantee insurance</li>
  </ul>

  <div class="listing-photo" role="img" aria-label="Photo of a row of red-brick terraced houses with rose bushes"></div>

  <p class="listing-copy">
    Office/retail to let - Fenwick Street, Marlcombe<br>
    New shop ground floor suitable for all uses.<br>
    Size - 23.3 sq/m (250.9 sq/ft) plus cellar.<br>
    Ideal for a small business startup!!!
    <span class="cta">Don't miss the opportunity.</span>
    The shop is situated in Abbey Lane,<br>
    Marlcombe . It is close to the Town Centre
  </p>

  <div class="open-bar">we are open 6 days a week</div>
  <div class="available-bar">Available</div>

  <div class="starburst">
    <svg width="145" height="145" viewBox="0 0 140 140" aria-hidden="true">
      <polygon fill="url(#goldGrad)" points="134,70 121.4,86.7 121.8,107.6 101.8,113.7 89.8,130.9 70,124 50.2,130.9 38.2,113.7 18.2,107.6 18.6,86.7 6,70 18.6,53.3 18.2,32.4 38.2,26.3 50.2,9.1 70,16 89.8,9.1 101.8,26.3 121.8,32.4 121.4,53.3"/>
    </svg>
    <span>24/7</span>
  </div>

  <div class="commercial">
    <p class="ask">Landlords! Did you know that<br>we also do commercial lettings?</p>
    <p class="call">Call us on</p>
    <p class="phone">01592738164</p>
    <p class="best">for best offer in the area</p>
  </div>

  <div class="socials">
    <span>Feedline</span><span>Skylark</span><span>Circlebook</span><span>Reeltime</span>
  </div>

  <div class="partners">
    <span>leasewell</span><span>KLT</span><span>Homeroost</span><span>WMA</span>
  </div>
</main>
</body>
</html>
```